KalVorin73' Website/Logo Design

We need a website and Logo design for our company called "kalvorin1973". We will be designing generic and mainly custom made clothing (t shirts, sweaters, hoodies, hats, caps, leggings etc) with other products of electronics and every day products with side sells. We want a catchy but easy to navigate website to use on our SHOPIFY website.
Updates

Designs look the same

Need extra days to review

Target Market(s)

Anyone that is interested in purchasing custom design clothing.

Logo Text

KalVorin73'

Number of Pages Required

1 page

Other font styles liked:
• Microbrew

Colors

Designer to choose colors to be used in the design.

```html
<!DOCTYPE html>
<html lang="en">
<head>
<meta charset="utf-8">
<title>KalVorin73' — Custom Clothing</title>
<link href="https://fonts.googleapis.com/css2?family=Roboto:wght@400;500;700&family=Roboto+Condensed:wght@400;700&display=swap" rel="stylesheet">
<style>
:root{
  --accent:#e2343c;
  --ink:#222222;
  --muted:#777777;
  --line:#e3e3e3;
  --soft:#f4f4f4;
  --footer:#1e1e1e;
  --footer-deep:#151515;
  --white:#ffffff;
}
*{box-sizing:border-box;margin:0;padding:0}
html,body{width:1200px;height:2500px;overflow:hidden}
body{font-family:'Roboto',sans-serif;color:var(--ink);background:var(--white);position:relative}
.wrap{width:860px;margin:0 auto;position:relative}
.cond{font-family:'Roboto Condensed',sans-serif}

/* top bar */
.topbar{height:30px;background:var(--soft);border-bottom:1px solid var(--line);font-size:10px;color:var(--muted);display:flex;align-items:center;justify-content:space-between;padding:0 170px}
.topbar .links span{margin-right:14px;text-transform:uppercase}
.topbar .right{display:flex;align-items:center;gap:8px}
.social{width:16px;height:16px;background:#cfcfcf;display:inline-block}

/* header */
.header{height:92px;display:flex;align-items:center;justify-content:space-between;padding:0 170px}
.brand{display:flex;align-items:center;gap:12px}
.brand-dot{width:34px;height:34px;border-radius:50%;background:var(--accent)}
.brand-name{font-family:'Roboto Condensed',sans-serif;font-weight:700;font-size:30px;color:var(--ink)}
.contact{display:flex;align-items:center;gap:22px;font-size:11px;color:var(--muted)}
.contact .lines div{display:flex;align-items:center;gap:6px;margin:3px 0}
.phone-box{border:1px solid var(--line);padding:7px 12px;border-radius:3px;display:flex;align-items:center;gap:6px;color:var(--ink)}

/* nav */
.nav{height:44px;border-top:1px solid var(--line);border-bottom:1px solid var(--line);display:flex;align-items:center;justify-content:space-between;padding:0 170px}
.nav ul{list-style:none;display:flex;gap:28px;font-size:11px;font-weight:700;text-transform:uppercase}
.nav li.active{color:var(--accent)}
.nav .tools{display:flex;align-items:center;gap:24px;font-size:10px}
.cart{display:flex;align-items:center;gap:8px}
.cart b{display:block;font-size:11px}

/* hero */
.hero{height:500px;margin-top:4px;position:relative;background:linear-gradient(100deg,#6b5a4a 0%,#a49383 30%,#d8cdc2 55%,#c8b5a2 75%,#8e7663 100%)}
.badge{position:absolute;left:150px;top:110px;width:250px;height:250px;border-radius:50%;background:rgba(40,36,34,.92);border:6px solid rgba(255,255,255,.5);color:var(--white);text-align:center;font-family:'Roboto Condensed',sans-serif}
.badge small{display:block;margin-top:62px;font-size:11px;letter-spacing:1px}
.badge strong{display:block;font-size:60px;line-height:.95;font-weight:700}
.badge-off{position:absolute;left:360px;top:175px;width:130px;height:130px;border-radius:50%;background:var(--white);text-align:center;font-family:'Roboto Condensed',sans-serif;font-weight:700;box-shadow:0 2px 8px rgba(0,0,0,.2)}
.badge-off span{display:block;margin-top:24px;font-size:22px}
.badge-off em{font-style:normal;display:block;font-size:54px;line-height:1;color:var(--accent)}

/* products */
.section-title{text-align:center;font-family:'Roboto Condensed',sans-serif;font-weight:700;font-size:34px;display:flex;align-items:center;justify-content:center;gap:18px}
.section-title::before,.section-title::after{content:"";width:60px;height:2px;background:var(--ink)}
.products{padding-top:50px}
.tabs{display:flex;justify-content:center;gap:34px;font-size:11px;text-transform:uppercase;margin-top:34px;color:var(--muted)}
.tabs .on{color:var(--ink);font-weight:700}
.cards{display:flex;gap:20px;margin-top:28px}
.card{width:273px;text-align:center}
.card .shot{height:280px;border:1px solid var(--line);padding:10px}
.card .shot div{width:100%;height:100%}
.card h3{font-size:11px;font-weight:700;margin-top:22px;text-transform:uppercase}
.price{display:flex;justify-content:space-between;padding:0 40px;font-size:11px;margin-top:16px;color:var(--muted)}
.price s{color:#aaa}
.btns{display:flex;justify-content:space-between;margin-top:38px}
.btn{width:128px;height:30px;border:1px solid #cfcfcf;font-size:9px;font-weight:700;display:flex;align-items:center;justify-content:center;text-transform:uppercase}
.divider{height:1px;background:var(--line);margin:60px 0 0}

/* promo */
.promo{display:grid;grid-template-columns:430px 206px 208px;grid-template-rows:178px 178px;gap:8px;margin-top:50px}
.promo .big{grid-row:1/3;position:relative;background:linear-gradient(120deg,#e9e3dc,#c9b7a8 55%,#8f7b6d)}
.promo .big .tag{position:absolute;left:0;right:0;top:200px;text-align:center;font-family:'Roboto Condensed',sans-serif;font-weight:700}
.promo .big .tag b{display:block;font-size:30px;color:var(--ink)}
.promo .big .tag span{display:block;font-size:14px;margin-top:14px;letter-spacing:1px}
.promo .mid{grid-row:1/3;background:linear-gradient(180deg,#5c5a58,#2f6b46 45%,#4a6a8c)}
.promo .cap{background:linear-gradient(160deg,#f2f2f2,#cfcfcf)}
.promo .hood{background:linear-gradient(160deg,#c9d8e6,#6f8fb0)}

/* blogs */
.blogs{display:flex;gap:14px;margin-top:36px}
.blog-intro{width:340px}
.blog-intro h2{font-family:'Roboto Condensed',sans-serif;font-weight:700;font-size:34px}
.blog-intro p{font-size:10px;color:var(--muted);line-height:1.6;margin-top:16px}
.arrows{display:flex;gap:6px;margin-top:18px}
.arrows span{width:20px;height:20px;border:1px solid #ccc;display:flex;align-items:center;justify-content:center;font-size:10px}
.blog-card{width:246px;height:186px;position:relative}
.blog-card .more{position:absolute;left:20px;bottom:18px;background:var(--white);font-size:8px;font-weight:700;padding:5px 10px}
.b1{background:linear-gradient(130deg,#d9c3a8,#8a6a4f 60%,#b49174)}
.b2{background:linear-gradient(130deg,#f0e7d8,#c7a889 60%,#e3d3c0)}

/* features */
.features{display:flex;justify-content:space-between;margin-top:58px;padding:14px 0;border-top:1px solid var(--line);border-bottom:1px solid var(--line)}
.feature{display:flex;align-items:center;gap:12px}
.feature b{display:block;font-family:'Roboto Condensed',sans-serif;font-size:15px;text-transform:uppercase}
.feature small{font-size:9px;color:var(--muted)}
.feature+.feature{border-left:1px solid var(--line);padding-left:30px}

/* footer */
.footer{position:absolute;left:0;right:0;top:2140px;height:360px;background:var(--footer);color:#bdbdbd}
.footer .wrap{display:flex;justify-content:space-between;padding-top:44px}
.footer h4{color:var(--white);font-size:11px;font-weight:700;text-transform:uppercase;margin-bottom:16px}
.footer p{font-size:9px;line-height:1.7;width:230px}
.footer ul{list-style:none;font-size:9px;line-height:2.1;text-transform:uppercase}
.footer .socials{display:flex;gap:6px;margin-top:16px}
.footer .socials span{width:18px;height:18px;background:#444}
.cols{display:flex;gap:70px}
.legal{position:absolute;left:0;right:0;bottom:0;height:44px;background:var(--footer-deep);font-size:9px;display:flex;align-items:center;justify-content:space-between;padding:0 170px;text-transform:uppercase}
.legal nav{display:flex;gap:18px}
</style>
</head>
<body>

<div class="topbar">
  <div class="links"><span>My Account</span><span>My Wishlist</span><span>Checkout</span></div>
  <div class="right"><span>USD</span><span>EN</span><i class="social"></i><i class="social"></i><i class="social"></i></div>
</div>

<header class="header">
  <div class="brand"><span class="brand-dot"></span><span class="brand-name">KalVorin73'</span></div>
  <div class="contact">
    <div class="lines">
      <div><svg width="10" height="10" viewBox="0 0 24 24"><path fill="#777" d="M6.6 10.8a15 15 0 0 0 6.6 6.6l2.2-2.2a1 1 0 0 1 1-.25 11.4 11.4 0 0 0 3.6.57 1 1 0 0 1 1 1V20a1 1 0 0 1-1 1A17 17 0 0 1 3 4a1 1 0 0 1 1-1h3.5a1 1 0 0 1 1 1c0 1.25.2 2.45.57 3.6a1 1 0 0 1-.25 1z"/></svg>Mon-Sat 9-6</div>
      <div><svg width="10" height="10" viewBox="0 0 24 24"><path fill="#777" d="M12 2a7 7 0 0 0-7 7c0 5.25 7 13 7 13s7-7.75 7-13a7 7 0 0 0-7-7zm0 9.5A2.5 2.5 0 1 1 12 6.5a2.5 2.5 0 0 1 0 5z"/></svg>Find a store</div>
    </div>
    <div class="phone-box"><svg width="11" height="11" viewBox="0 0 24 24"><path fill="#e2343c" d="M6.6 10.8a15 15 0 0 0 6.6 6.6l2.2-2.2a1 1 0 0 1 1-.25 11.4 11.4 0 0 0 3.6.57 1 1 0 0 1 1 1V20a1 1 0 0 1-1 1A17 17 0 0 1 3 4a1 1 0 0 1 1-1h3.5a1 1 0 0 1 1 1c0 1.25.2 2.45.57 3.6a1 1 0 0 1-.25 1z"/></svg>+1 (555) 014 2270</div>
  </div>
</header>

<nav class="nav">
  <ul><li class="active">Home</li><li>About Us</li><li>Collection</li><li>Our Products</li><li>Shop</li><li>Contact Us</li></ul>
  <div class="tools">
    <svg width="14" height="14" viewBox="0 0 24 24"><circle cx="10" cy="10" r="6.5" fill="none" stroke="#222" stroke-width="2"/><path d="M15 15l6 6" stroke="#222" stroke-width="2"/></svg>
    <div class="cart">
      <svg width="22" height="22" viewBox="0 0 24 24"><path fill="#222" d="M7 18a2 2 0 1 0 0 4 2 2 0 0 0 0-4zm10 0a2 2 0 1 0 0 4 2 2 0 0 0 0-4zM3 2h3l2.7 11h9.6l2.2-7H7.2"/><path d="M3 2h3l2.7 11h9.6l2.2-7H7" fill="none" stroke="#222" stroke-width="2"/></svg>
      <div><b>Shopping Cart</b>0 item(s) - $0.00</div>
    </div>
  </div>
</nav>

<section class="hero" role="img" aria-label="Photo of a smiling young woman in a white top with long hair blowing">
  <div class="badge"><small>IT HAS FINALLY STARTED</small><strong>HUGE<br>SALE</strong></div>
  <div class="badge-off"><span>UP TO</span><em>70<small style="font-size:22px">%</small></em></div>
</section>

<section class="products wrap">
  <h2 class="section-title">OUR PRODUCTS</h2>
  <div class="tabs"><span class="on">Best Seller</span><span>New Arrivals</span><span>Random</span><span>Special</span><span>Latest</span></div>
  <div class="cards">
    <article class="card">
      <div class="shot"><div role="img" aria-label="Product photo of a green knit sweater" style="background:linear-gradient(180deg,#ece9e4,#2f7a4a 40%,#2a5f3e)"></div></div>
      <h3>Green Sweaters</h3>
      <div class="price"><s>$199.00</s><span>$80.00</span></div>
      <div class="btns"><span class="btn">View Details</span><span class="btn">Add to Cart</span></div>
    </article>
    <article class="card">
      <div class="shot"><div role="img" aria-label="Product photo of a plain white t-shirt" style="background:linear-gradient(180deg,#f6f6f6,#e4e4e4 60%,#d6d6d6)"></div></div>
      <h3>White T Shirts</h3>
      <div class="price"><s>$199.00</s><span>$80.00</span></div>
      <div class="btns"><span class="btn">View Details</span><span class="btn">Add to Cart</span></div>
    </article>
    <article class="card">
      <div class="shot"><div role="img" aria-label="Product photo of a grey zip hoodie" style="background:linear-gradient(180deg,#f3f3f3,#a5a9ae 50%,#8c9095)"></div></div>
      <h3>Hoodies</h3>
      <div class="price"><s>$199.00</s><span>$80.00</span></div>
      <div class="btns"><span class="btn">View Details</span><span class="btn">Add to Cart</span></div>
    </article>
  </div>
</section>
<div class="divider"></div>

<section class="wrap">
  <div class="promo">
    <div class="big" role="img" aria-label="Photo of a woman in a wide hat and light coat">
      <div class="tag"><b>SALE UP TO 70% OFF</b><span>WOMEN</span></div>
    </div>
    <div class="mid" role="img" aria-label="Photo of a woman wearing a green sweater and jeans"></div>
    <div class="cap" role="img" aria-label="Photo of a black baseball cap"></div>
    <div class="hood" role="img" aria-label="Photo of a person in a hooded sweatshirt"></div>
  </div>

  <div class="blogs">
    <div class="blog-intro">
      <h2>LATEST BLOGS</h2>
      <p>Fresh notes from our studio on custom prints, fabric care and styling tips for every season. Read the newest stories and find ideas for your next made-to-order piece here today.</p>
      <div class="arrows"><span>‹</span><span>›</span></div>
    </div>
    <div class="blog-card b1" role="img" aria-label="Photo of friends shopping with bags"><span class="more">READ MORE</span></div>
    <div class="blog-card b2" role="img" aria-label="Photo of a smiling woman holding shopping bags"><span class="more">READ MORE</span></div>
  </div>

  <div class="features">
    <div class="feature">
      <svg width="34" height="24" viewBox="0 0 34 24"><path d="M1 4h20v14H1zM21 9h7l5 5v4h-12z" fill="none" stroke="#222" stroke-width="1.6"/><circle cx="7" cy="20" r="2.5" fill="#fff" stroke="#222" stroke-width="1.6"/><circle cx="27" cy="20" r="2.5" fill="#fff" stroke="#222" stroke-width="1.6"/></svg>
      <div><b>Fast Delivery</b><small>We deliver to your door quickly</small></div>
    </div>
    <div class="feature">
      <svg width="26" height="26" viewBox="0 0 24 24"><rect x="6" y="2" width="12" height="20" rx="2" fill="none" stroke="#222" stroke-width="1.6"/><circle cx="12" cy="18.5" r="1" fill="#222"/></svg>
      <div><b>24/7 Customer Suport</b><small>Friendly help around the clock</small></div>
    </div>
    <div class="feature">
      <svg width="26" height="26" viewBox="0 0 24 24"><circle cx="12" cy="12" r="9.5" fill="none" stroke="#222" stroke-width="1.6"/><path d="M12 7v5l3 2" fill="none" stroke="#222" stroke-width="1.6"/></svg>
      <div><b>30 Day Money Back</b><small>Easy returns within thirty days</small></div>
    </div>
  </div>
</section>

<footer class="footer">
  <div class="wrap">
    <div>
      <h4>About Us</h4>
      <p>KalVorin73' makes custom clothing to order: tees, sweaters, hoodies, caps and more, printed with care and shipped fast. Reach us any day at hello@kalvorin73.example.</p>
      <div class="socials"><span></span><span></span><span></span></div>
    </div>
    <div>
      <h4>Customer Services</h4>
      <div class="cols">
        <ul><li>Contact Us</li><li>About Us</li><li>Delivery Information</li><li>Privacy Policy</li><li>Terms &amp; Conditions</li></ul>
        <ul><li>Brands</li><li>Gift Certificates</li><li>Affiliates</li><li>Specials</li><li>Site Map</li></ul>
      </div>
    </div>
    <div>
      <h4>My Account</h4>
      <ul><li>My Account</li><li>Order History</li><li>Wish List</li><li>Newsletter</li><li>Returns</li></ul>
    </div>
  </div>
  <div class="legal">
    <span>Copyright © KalVorin73' Clothing. All rights reserved</span>
    <nav><span>Home</span><span>About Us</span><span>Collection</span><span>Our Products</span><span>Shop</span><span>Contact Us</span></nav>
  </div>
</footer>

</body>
</html>
```